Silver Heron Staffing Agency

I need to make a brochure/catalogue that represent our company, telling our clients what we do, our values, fields of industry that we taken care of, so they know who we are, what we did, and how we do it.
I do have a logo and simple brochure design before that i really need to upgrade (i will give it as an example on this attachment).

What I want in the new design is :
1. More pictures and little bit of explanation in each industry we work with.
2. Attractive design that make people LOOK at the brochure and not just throw it in the trash.
3. Still use the combination color of the company logo itself, which is Golden Brown.

```html
<!DOCTYPE html>
<html lang="en">
<head>
<meta charset="utf-8">
<title>Silver Heron Staffing Agency – Trifold Brochure</title>
<link href="https://fonts.googleapis.com/css2?family=Lato:wght@400;700;900&family=Roboto+Condensed:wght@400;700&display=swap" rel="stylesheet">
<style>
:root{
  --gold:#c9a24a;
  --gold-dark:#a8873a;
  --gold-light:#dcc07a;
  --ink:#222;
  --text:#444;
  --black:#111;
  --charcoal:#2b2b2b;
  --white:#fff;
  --canvas:#d9dadc;
}
*{box-sizing:border-box;margin:0;padding:0}
html,body{width:879px;height:1200px;overflow:hidden;background:var(--canvas);font-family:"Lato",sans-serif;color:var(--text)}
.sheet{position:absolute;left:123px;width:646px;height:503px;box-shadow:0 14px 14px -8px rgba(0,0,0,.35)}
.sheet--outside{top:67px}
.sheet--inside{top:622px}
.panel{position:absolute;top:0;height:503px;overflow:hidden}
.panel--a{left:0;width:215px}
.panel--b{left:215px;width:216px}
.panel--c{left:431px;width:215px}
.bg-white{background:var(--white)}
.bg-black{background:linear-gradient(160deg,#353535 0%,#151515 55%,#0b0b0b 100%);color:var(--white)}
.abs{position:absolute}
.footer{position:absolute;left:0;right:0;top:469px;height:22px;background:var(--gold);color:var(--white);font-size:7.5px;display:flex;align-items:center;justify-content:center;gap:5px}
.footer svg{width:8px;height:8px}
.photo{background:linear-gradient(135deg,#6f6a62,#a49a88 50%,#4a4540)}
.gold-text{color:var(--gold)}
.h-cond{font-family:"Roboto Condensed",sans-serif}
.brand{font-family:"Lato",sans-serif;font-weight:700;color:var(--gold);letter-spacing:.5px;display:flex;align-items:center;gap:5px;justify-content:center}
.brand i{display:block;width:9px;height:9px;background:var(--gold)}
/* outside left */
.hero-strip{left:0;top:0;width:215px;height:12px;background:linear-gradient(90deg,var(--gold-dark),var(--gold-light))}
.hero-photo{left:0;top:10px;width:215px;height:142px;clip-path:polygon(0 0,100% 0,100% 78%,0 100%);background:linear-gradient(180deg,#8fa3bd 0%,#4d5666 60%,#2c2f36 100%)}
.industries-title{left:14px;top:176px;width:195px;font-size:10px;color:var(--ink);line-height:13px;text-transform:uppercase}
.rule{left:14px;top:213px;width:186px;height:1px;background:#ccc}
.lead{left:14px;top:221px;width:190px;font-size:8.3px;line-height:12.5px;color:#555}
.bubble{top:283px;width:65px;height:65px;border-radius:50%;border:2px solid var(--gold)}
.industry-list{left:12px;top:366px;width:200px;display:grid;grid-template-columns:94px 100px;row-gap:6px;font-size:8.5px;color:var(--ink)}
.industry-list li{list-style:none;display:flex;align-items:center;gap:6px;height:16px}
.dot{width:16px;height:16px;border-radius:50%;background:var(--gold-light);border:1px solid var(--gold);flex:none;display:flex;align-items:center;justify-content:center}
.dot::after{content:"";width:6px;height:6px;border-radius:50%;background:var(--charcoal)}
/* outside middle */
.circle-photo{width:136px;height:136px;border-radius:50%;border:3px solid var(--gold);background:linear-gradient(160deg,#e8e2d8,#b9ab95 60%,#7d6f5c)}
.tag{background:linear-gradient(90deg,var(--gold-dark),var(--gold-light));color:var(--black);font-weight:900;font-size:10px;display:flex;align-items:center;justify-content:center}
.blurb{left:12px;width:192px;font-size:7.8px;line-height:11px;text-align:center;color:var(--gold)}
.contact{left:0;width:216px;text-align:center;font-size:7px;line-height:10px;color:var(--white)}
/* outside right */
.cover-photo{left:0;top:84px;width:215px;height:225px;background:linear-gradient(160deg,#d8b888 0%,#a98d63 40%,#6f6a5d 100%)}
.cover-black{left:0;top:283px;width:215px;height:160px;background:linear-gradient(180deg,#1c1c1c,#2a2a2a);clip-path:polygon(0 8%,100% 0,100% 100%,0 100%)}
.cover-title{left:0;top:340px;width:215px;text-align:center;font-weight:900;font-size:23px;line-height:27px;color:var(--gold);text-transform:uppercase}
.cover-strip{left:0;top:438px;width:215px;height:31px;background:linear-gradient(90deg,#8c7754,#b89c6a,#6d6252);clip-path:polygon(0 0,100% 12%,100% 100%,0 100%)}
/* inside */
.section-title{font-weight:900;font-size:15px;color:var(--ink);text-transform:uppercase}
.section-title span{color:var(--gold)}
.bg-black .section-title{color:var(--gold)}
.body{font-size:7.1px;line-height:9.2px;text-align:justify}
.sub{display:flex;align-items:center;gap:6px;font-size:12px;color:var(--gold);text-transform:uppercase}
.sub svg{width:24px;height:22px}
.item-title{font-size:7.5px;color:var(--gold)}
.gold-band{top:151px;height:150px;background:linear-gradient(180deg,#d7bd7c,#c5a456)}
.label-black{background:var(--black);color:var(--white);font-weight:900;font-size:10.5px;line-height:13px;text-align:center;display:flex;align-items:center;justify-content:center}
.why{display:flex;gap:5px}
.why svg{flex:none;width:9px;height:9px;margin-top:1px}
</style>
</head>
<body>

<!-- OUTSIDE -->
<section class="sheet sheet--outside">
  <!-- Industries panel -->
  <div class="panel panel--a bg-white">
    <div class="abs hero-photo" role="img" aria-label="Photo of job candidates in business attire seated in a row waiting for interviews"></div>
    <div class="abs hero-strip"></div>
    <h2 class="abs industries-title"><span class="gold-text" style="font-weight:700">We find</span> the best people for the following industries</h2>
    <div class="abs rule"></div>
    <p class="abs lead">Our success is based on our unique ability to identify top candidates and the high-quality professional development of our candidates.</p>
    <div class="abs bubble" style="left:12px;background:linear-gradient(160deg,#dfe9f3,#5d8fc4)" role="img" aria-label="Photo of a medical worker"></div>
    <div class="abs bubble" style="left:74px;background:linear-gradient(160deg,#e7d8c4,#8b6c4b)" role="img" aria-label="Photo of a hospitality worker"></div>
    <div class="abs bubble" style="left:136px;background:linear-gradient(160deg,#cfd6a5,#6f7a3d)" role="img" aria-label="Photo of a warehouse worker in a hard hat"></div>
    <ul class="abs industry-list">
      <li><span class="dot"></span>Warehousing</li>
      <li><span class="dot"></span>Transposition</li>
      <li><span class="dot"></span>Hospitality</li>
      <li><span class="dot"></span>Landfill</li>
      <li><span class="dot"></span>Casino</li>
      <li><span class="dot"></span>Food Handling</li>
      <li><span class="dot"></span>Paper Mailing</li>
      <li><span class="dot"></span>And much more</li>
    </ul>
    <div class="footer"><svg viewBox="0 0 10 10"><circle cx="5" cy="5" r="4.3" fill="none" stroke="#fff"/><path d="M.7 5h8.6M5 .7c2.4 2.4 2.4 6.2 0 8.6M5 .7c-2.4 2.4-2.4 6.2 0 8.6" fill="none" stroke="#fff" stroke-width=".7"/></svg>www.silverheronstaffingservices.com</div>
  </div>

  <!-- Contract panel -->
  <div class="panel panel--b bg-black">
    <div class="abs circle-photo" style="left:39px;top:27px" role="img" aria-label="Photo of a housekeeper making a bed"></div>
    <div class="abs tag" style="left:53px;top:149px;width:110px;height:23px">Contract To Hire</div>
    <p class="abs blurb" style="top:188px">Reduce the risk of making a bad hire by evaluating a candidate's performance in your work environment. You can choose to add workers to your permanent team or requesting another worker for your evaluation.</p>
    <p class="abs blurb" style="top:252px">With more than 18 years of experience Silver Heron Staffing has provided staffing services all throughout Pennsylvania, New York, New Jersey, Delaware, Virginia &amp; Georgia.</p>
    <div class="abs brand" style="left:0;top:330px;width:216px;font-size:9px"><i></i>SILVER HERON INC.</div>
    <p class="abs contact" style="top:393px">555 214 0187</p>
    <p class="abs contact" style="top:409px">48 Aspen Ln, Ste 210<br>Cedar Grove,NJ 07009-2210</p>
    <p class="abs contact" style="top:441px">cs@silverheronstaffingservices.com<br>www.silverheronstaffingservices.com</p>
    <div class="footer"><svg viewBox="0 0 10 10"><circle cx="5" cy="5" r="4.3" fill="none" stroke="#fff"/><path d="M.7 5h8.6M5 .7c2.4 2.4 2.4 6.2 0 8.6M5 .7c-2.4 2.4-2.4 6.2 0 8.6" fill="none" stroke="#fff" stroke-width=".7"/></svg>www.silverheronstaffingservices.com</div>
  </div>

  <!-- Cover panel -->
  <div class="panel panel--c bg-white">
    <div class="abs brand" style="left:0;top:34px;width:215px;font-size:11px"><i></i>SILVER HERON INC.</div>
    <div class="abs" style="left:0;top:82px;width:215px;height:2px;background:var(--gold)"></div>
    <div class="abs cover-photo" role="img" aria-label="Photo of a smiling warehouse worker in a hard hat and safety vest carrying boxes"></div>
    <div class="abs cover-black"></div>
    <h1 class="abs cover-title">Your best way<br>to succeed</h1>
    <div class="abs cover-strip" role="img" aria-label="Photo of warehouse shelving"></div>
    <div class="footer"><svg viewBox="0 0 10 10"><circle cx="5" cy="5" r="4.3" fill="none" stroke="#fff"/><path d="M.7 5h8.6M5 .7c2.4 2.4 2.4 6.2 0 8.6M5 .7c-2.4 2.4-2.4 6.2 0 8.6" fill="none" stroke="#fff" stroke-width=".7"/></svg>www.silverheronstaffingservices.com</div>
  </div>
</section>

<!-- INSIDE -->
<section class="sheet sheet--inside">
  <!-- About panel -->
  <div class="panel panel--a bg-black">
    <h2 class="abs section-title" style="left:14px;top:26px">About <span style="color:var(--white)">us</span></h2>
    <p class="abs body" style="left:14px;top:56px;width:190px;font-size:7.3px">Our ethics are a critical building block of our business. Our own success is based on adherence to the highest ethical standards; long-term client relationships, the ability to identify top candidates, and the high-quality professional development of Silver Heron Staffing professionals protecting the confidentiality and interests of clients and candidates.</p>

    <div class="abs sub" style="left:14px;top:138px"><svg viewBox="0 0 24 22"><circle cx="9" cy="6" r="4" fill="none" stroke="#c9a24a" stroke-width="1.6"/><circle cx="17" cy="7" r="3" fill="none" stroke="#c9a24a" stroke-width="1.4"/><path d="M2 20c0-5 3-7 7-7s7 2 7 7M14 13c3 0 7 1 7 6" fill="none" stroke="#c9a24a" stroke-width="1.6"/></svg>Culture</div>
    <p class="abs body" style="left:14px;top:169px;width:190px">Silver Heron believes in equal opportunity for all, regardless of gender, race, ethic, origin, religion, or handicap. The staffing policies and practices of Silver Heron Staffing for our organization, our clients and candidates are fully non-discriminatory. Our employees are our most valuable asset. We strive to create a work environment of professionalism, trust and respect that will continuously provide our staff with motivation, challenge, and professional growth to aim our most important goal; CLIENT SATISFACTION.</p>

    <div class="abs sub" style="left:14px;top:276px"><svg viewBox="0 0 24 22"><rect x="2" y="7" width="18" height="13" rx="1" fill="none" stroke="#c9a24a" stroke-width="1.6"/><path d="M5 12h6M5 16h4" stroke="#c9a24a" stroke-width="1.4"/><circle cx="15" cy="13" r="2" fill="#c9a24a"/><path d="M13 3c3-2 6-2 9 1" fill="none" stroke="#c9a24a" stroke-width="1.4"/></svg>Mission</div>
    <p class="abs body" style="left:14px;top:307px;width:190px">Silver Heron is more than a staffing company; we want to become your business partner. We understand that payroll and employee-service overhead can be one of the largest expenses for your business. Through our partnership-network programs Silver Heron can help you reduce the hard-costs of your business expenses. We take responsibility for all our placed employees, including payroll taxes and benefits.</p>

    <div class="abs sub" style="left:14px;top:391px"><svg viewBox="0 0 24 22"><rect x="3" y="3" width="14" height="17" rx="1" fill="none" stroke="#c9a24a" stroke-width="1.6"/><path d="M6 9l2 2 4-4M6 15h7" fill="none" stroke="#c9a24a" stroke-width="1.4"/><path d="M17 10l4 3-4 3z" fill="#c9a24a"/></svg>Our process</div>
    <p class="abs body" style="left:14px;top:419px;width:190px">Our screening process includes a thorough interview with each potential candidate to give us insight into the candidate's previous work history, skills, communication abilities and career goals as well as reference checks with their previous employers.</p>
    <div class="footer"><svg viewBox="0 0 10 10"><circle cx="5" cy="5" r="4.3" fill="none" stroke="#fff"/><path d="M.7 5h8.6M5 .7c2.4 2.4 2.4 6.2 0 8.6M5 .7c-2.4 2.4-2.4 6.2 0 8.6" fill="none" stroke="#fff" stroke-width=".7"/></svg>www.silverheronstaffingservices.com</div>
  </div>

  <!-- Services panel -->
  <div class="panel panel--b bg-white">
    <h2 class="abs section-title" style="left:12px;top:26px">Our <span>services</span></h2>
    <div class="abs" style="left:12px;top:56px;width:194px">
      <p class="item-title">Employee Benefits:</p>
      <p class="body">Workers are paid on a timely weekly basis. Our system responds to worker's need for payment immediately.</p>
      <p class="item-title" style="margin-top:6px">Workers' Compensation:</p>
      <p class="body">We provide workers' compensation for our employees while on assignment. If an injury occurs, we handle all claims and expenses. Our safety and risk department will help reduce injuries and will ensure high rates of safety compliance.</p>
    </div>
    <div class="abs gold-band" style="left:0;width:216px"></div>
    <div class="abs circle-photo" style="left:39px;top:141px;width:134px;height:134px;background:linear-gradient(160deg,#cfd8c8,#8a9a6e 55%,#5c4a3a)" role="img" aria-label="Photo of a smiling worker holding a crate of strawberries in a greenhouse"></div>
    <div class="abs label-black" style="left:37px;top:233px;width:137px;height:36px">We Save you both<br>TIME and MONEY</div>
    <p class="abs" style="left:6px;top:280px;width:204px;text-align:center;font-size:7px;line-height:9.5px;color:var(--ink)">Competitive rates to keep your business on budget.<br>We bill only for employee's hours approved by you.</p>

    <h2 class="abs section-title" style="left:12px;top:316px">Why <span>staffing?</span></h2>
    <div class="abs" style="left:12px;top:349px;width:194px">
      <div class="why"><svg viewBox="0 0 10 10"><circle cx="5" cy="5" r="4.3" fill="none" stroke="#c9a24a"/><path d="M3 5l1.5 1.5L7 3.8" fill="none" stroke="#c9a24a"/></svg><div><p class="item-title">Avoid Unemployment Claims</p><p class="body">The temporary staff personnel is an employee of the staffing agency and not the business, there is no concern about the person filing for unemployment when their services are no longer needed by the business reducing overall operating and human resources costs.</p></div></div>
      <div class="why" style="margin-top:6px"><svg viewBox="0 0 10 10"><circle cx="5" cy="5" r="4.3" fill="none" stroke="#c9a24a"/><path d="M3 5l1.5 1.5L7 3.8" fill="none" stroke="#c9a24a"/></svg><div><p class="item-title">Improve Productivity</p><p class="body">By bringing in temporary staff to handle the extra work-load, your full-time employees can continue to focus on their main job tasks while maintaining their productivity.</p></div></div>
    </div>
    <div class="footer"><svg viewBox="0 0 10 10"><circle cx="5" cy="5" r="4.3" fill="none" stroke="#fff"/><path d="M.7 5h8.6M5 .7c2.4 2.4 2.4 6.2 0 8.6M5 .7c-2.4 2.4-2.4 6.2 0 8.6" fill="none" stroke="#fff" stroke-width=".7"/></svg>www.silverheronstaffingservices.com</div>
  </div>

  <!-- Values panel -->
  <div class="panel panel--c bg-white">
    <div class="abs brand" style="left:130px;top:20px;width:80px;font-size:7px;justify-content:flex-end"><i style="width:7px;height:7px"></i>SILVER HERON INC.</div>
    <div class="abs" style="left:10px;top:63px;width:196px">
      <p class="item-title">Availability and Flexibility</p>
      <p class="body" style="font-size:8px;line-height:10.6px">Our temporary staff has proven to be available and ready for work in a timely and efficient manner. Our services will be crafted to your needs and specifications ensuring that you are not forced into any unnecessary liabilities.</p>
    </div>
    <div class="abs gold-band" style="left:0;top:155px;width:215px;height:146px"></div>
    <div class="abs" style="left:10px;top:162px;width:196px;color:var(--ink)">
      <p class="body">Our business was built on a strong reputation for providing quality service. Part of that reputation stems from an unmatched focus on developing a deep understanding of the job market.</p>
      <p class="body" style="margin-top:10px">We believe that knowledge is a driving factor in staffing agency success, and we work with our clients and candidates so they are in the best position possible to accomplish their employment goals.</p>
      <p class="body" style="margin-top:10px">When you are looking for a qualified candidate or when you need a new job, trust the experts at Silver Heron Staffing Services. Let us put our world-class customer service and staffing expertise to work for you!</p>
    </div>
    <div class="abs" style="left:6px;top:349px;width:200px">
      <div class="why"><svg viewBox="0 0 10 10"><circle cx="5" cy="5" r="4.3" fill="none" stroke="#c9a24a"/><path d="M3 5l1.5 1.5L7 3.8" fill="none" stroke="#c9a24a"/></svg><div><p class="item-title">Increasing Flexibility</p><p class="body">Temporary employees can be brought in to cover the vacation of an employee or maternity leave or a seasonal work. Whether it is a few hours a week or on a full-time basis, using a staffing agency can avoid the permanent commitment that a full-time employee requires.</p></div></div>
      <div class="why" style="margin-top:6px"><svg viewBox="0 0 10 10"><circle cx="5" cy="5" r="4.3" fill="none" stroke="#c9a24a"/><path d="M3 5l1.5 1.5L7 3.8" fill="none" stroke="#c9a24a"/></svg><div><p class="item-title">Decrease Cost</p><p class="body">Employing temporary staff can decrease overhead costs such as overtime for regular, fulltime employees as well as additional benefits that the business does not have to provide to a temporary staff member.</p></div></div>
    </div>
    <div class="footer"><svg viewBox="0 0 10 10"><circle cx="5" cy="5" r="4.3" fill="none" stroke="#fff"/><path d="M.7 5h8.6M5 .7c2.4 2.4 2.4 6.2 0 8.6M5 .7c-2.4 2.4-2.4 6.2 0 8.6" fill="none" stroke="#fff" stroke-width=".7"/></svg>www.silverheronstaffingservices.com</div>
  </div>
</section>

</body>
</html>
```